Online Assistant Business needs sleek business card design

I need a contemporary / professional business card using the logo I have uploaded. I like simple clean designs. The business is an online (virtual) assistant business and my business card will be used at networking events and letter box dropped at local small to medium businesses.

Target Market(s)

Small to medium businesses

Industry/Entity Type

Consulting

Contact Information for Business Card

Corinne Wheatley
corinne@velqorahub.net.au
+ 61 (0) 491 570 156
www.velqorahub.net.au

```html
<!DOCTYPE html>
<html lang="en">
<head>
<meta charset="utf-8">
<title>Velqora Hub – Business Card</title>
<link rel="stylesheet" href="https://fonts.googleapis.com/css2?family=Arimo:wght@400;700&display=swap">
<style>
  :root {
    --page-bg: #ffffff;
    --card-bg: #ffffff;
    --brand-blue: #2193d3;
    --tint-blue: #e2f0f7;
    --tint-grey: #ebebeb;
    --rule-blue: #3a9fd6;
  }
  html, body {
    margin: 0;
    padding: 0;
    width: 1200px;
    height: 852px;
    overflow: hidden;
    background: var(--page-bg);
    font-family: "Arimo", Arial, sans-serif;
  }
  .canvas {
    position: relative;
    width: 1200px;
    height: 852px;
  }
  .card {
    position: absolute;
    left: 326px;
    top: 282px;
    width: 523px;
    height: 291px;
    background: var(--card-bg);
    overflow: hidden;
    box-shadow: 0 0 0 1px #f2f2f2;
  }
  .brand-decoration {
    position: absolute;
    left: 222px;
    top: 0;
    width: 301px;
    height: 291px;
    background: linear-gradient(120deg, var(--card-bg) 0%, var(--tint-blue) 40%, var(--tint-grey) 100%);
    opacity: 0.8;
  }
  .rule {
    position: absolute;
    left: 0;
    width: 100%;
    height: 1px;
    background: var(--rule-blue);
  }
  .rule--top { top: 104px; }
  .rule--bottom { top: 256px; }
  .brand {
    position: absolute;
    left: 39px;
    top: 12px;
    display: flex;
    flex-direction: column;
    align-items: center;
  }
  .brand-dot {
    width: 36px;
    height: 36px;
    border-radius: 50%;
    background: var(--brand-blue);
    margin-bottom: 14px;
  }
  .brand-name {
    font-size: 24px;
    font-weight: 400;
    line-height: 1;
    color: var(--brand-blue);
    letter-spacing: 0.5px;
  }
  .contact {
    position: absolute;
    left: 35px;
    top: 121px;
    color: var(--brand-blue);
    line-height: 1;
  }
  .contact p { margin: 0; white-space: nowrap; }
  .contact-name { font-size: 25px; font-weight: 700; }
  .contact-phone { font-size: 22px; margin-top: 9px !important; }
  .contact-email { font-size: 20px; margin-top: 19px !important; }
  .contact-web { font-size: 18px; margin-top: 9px !important; }
</style>
</head>
<body>
<main class="canvas">
  <section class="card">
    <div class="brand-decoration" role="img" aria-label="Large faint brand mark decoration"></div>
    <div class="rule rule--top"></div>
    <div class="rule rule--bottom"></div>
    <div class="brand">
      <span class="brand-dot"></span>
      <span class="brand-name">velqora hub</span>
    </div>
    <div class="contact">
      <p class="contact-name">Corinne Wheatley</p>
      <p class="contact-phone">+ 61 (0) 491 570 156</p>
      <p class="contact-email">corinne@velqorahub.net.au</p>
      <p class="contact-web">www.velqorahub.net.au</p>
    </div>
  </section>
</main>
</body>
</html>
```